qTrellis IT Website

We need a logo design for a new company in Jeffersonville, IN (serving predminately the Louisville, KY area). We merged Margo Information Systems (an IT staffing company) and Stat Wranglers (a business intelligence consulting group). Our logo was completed through Pixel Bazaar. We are doing a soft launch as we want one web page with just basic information and link that to the existing web pages we have: 1) www.margoinfosys-example.com and 2) www.statwranglers-example.com.
The 3 tabs we have in mind are:
Services/News/About Us. Under Services are: IT Staffing, Analytics/BI, Strategic Outsourcing, and CIO Services. Under About Us, we have History, Leadership and Contact Us. No submenu for News.
We also want to have the current companies' sites as clickable links. One should be IT Staffing (directed to www.margoinfosys-example.com) and the other should be Business Intelligence/Data Analytics (directed to www.statwranglers-example.com).
Target Market(s)
IT professionals and clients needing IT services
Industry/Entity Type
It Company
Coding
Coded - Design and coding required
Number of Pages Required
4 page
Look and feel

```html
<!DOCTYPE html>
<html lang="en">
<head>
<meta charset="utf-8">
<title>Our Services and Our Team</title>
<link rel="stylesheet" href="https://fonts.googleapis.com/css2?family=Oswald:wght@400&family=Lato:wght@300;400&display=swap">
<style>
  :root{
    --brand-blue:#1a5795;
    --accent-blue:#2d9ad8;
    --ink:#111111;
    --text:#222222;
    --panel:#fbfbf9;
    --page:#ffffff;
    --team-bg:#f2f2f2;
    --divider-dark:#555555;
    --footer-edge:#2a2a2a;
  }
  *{margin:0;padding:0;box-sizing:border-box}
  html,body{width:1200px;height:967px;overflow:hidden;background:var(--page)}
  body{position:relative;font-family:"Lato",sans-serif;color:var(--text)}
  .heading{font-family:"Oswald",sans-serif;font-weight:400;position:absolute;white-space:nowrap}

  /* Services */
  .services{position:absolute;left:0;top:0;width:1200px;height:470px;background:var(--page)}
  .services-panel{position:absolute;left:132px;top:0;width:936px;height:470px;background:var(--panel)}
  .section-title{left:0;width:1200px;text-align:center;font-size:30px;line-height:1}
  .services .section-title{top:43px;color:var(--brand-blue)}
  .divider{position:absolute;height:10px}
  .divider .line{position:absolute;top:4px;height:2px;background:var(--ink)}
  .divider .dot{position:absolute;top:0;width:11px;height:11px;border-radius:2px}
  .service-photo{position:absolute;left:146px;top:131px;width:296px;height:296px;border-radius:50%;
    background:radial-gradient(circle at 40% 35%,#f4f9fd 0%,#cfe4f3 45%,#5a98c9 75%,#1f3f63 100%);
    border:1px solid #b8b8b8}
  .service-name{left:470px;top:168px;font-size:29px;color:var(--ink)}
  .service-text{position:absolute;left:471px;top:224px;width:595px;font-size:11.3px;line-height:17.6px;font-weight:400;color:var(--text)}
  .read-more{position:absolute;left:472px;top:327px;width:136px;height:32px;background:var(--accent-blue);
    color:#fff;font-family:"Oswald",sans-serif;font-size:16px;line-height:32px;text-align:center;border-radius:2px;text-decoration:none}
  .slider-controls{position:absolute;left:1012px;top:401px;width:56px;height:29px;border:1px solid var(--accent-blue);display:flex;background:#fff}
  .slider-controls span{flex:1;display:flex;align-items:center;justify-content:center}
  .slider-controls span+span{border-left:1px solid var(--accent-blue)}

  /* Team */
  .team{position:absolute;left:0;top:470px;width:1200px;height:494px;background:var(--team-bg)}
  .team .section-title{top:38px;color:var(--ink)}
  .member{position:absolute;top:125px;width:260px;text-align:center}
  .member .portrait{margin:0 auto;width:254px;height:254px;border-radius:50%;border:2px solid var(--brand-blue);overflow:hidden;position:relative}
  .portrait.light{background:radial-gradient(circle at 50% 40%,#e9c6a8 0%,#f3ece6 40%,#ffffff 70%)}
  .portrait.dark{background:radial-gradient(circle at 50% 40%,#b89a86 0%,#6b7378 40%,#3d454b 80%)}
  .portrait.suit{background:radial-gradient(circle at 50% 40%,#e2b899 0%,#f0ebe6 45%,#9a9a9a 85%)}
  .social-band{position:absolute;left:0;bottom:0;width:100%;height:40px;background:var(--accent-blue);display:flex;justify-content:center;align-items:center;gap:14px;padding-bottom:4px}
  .social-band i{width:12px;height:12px;border-radius:50%;background:#fff;display:block}
  .member-name{font-family:"Oswald",sans-serif;font-size:22px;color:var(--brand-blue);margin-top:7px;line-height:1.15}
  .member-role{display:inline-block;background:var(--brand-blue);color:#fff;font-size:14px;line-height:21px;padding:0 5px;margin-top:1px}
  .team-arrow{position:absolute;top:233px}
  .footer-edge{position:absolute;left:0;top:964px;width:1200px;height:3px;background:var(--footer-edge)}
</style>
</head>
<body>

<section class="services">
  <div class="services-panel"></div>
  <h2 class="heading section-title">OUR SERVICES</h2>
  <div class="divider" style="left:469px;top:85px;width:250px">
    <span class="line" style="left:0;width:114px"></span>
    <span class="dot" style="left:119px;background:var(--brand-blue)"></span>
    <span class="line" style="left:135px;width:115px"></span>
  </div>
  <div class="service-photo" role="img" aria-label="Photo of two business people silhouetted beside a laptop in a bright office"></div>
  <h3 class="heading service-name">Information Systems</h3>
  <p class="service-text">Lorem Ipsum is simply dummy text of the printing and typesetting industry. Lorem Ipsum has been the industry's standard dummy text ever since the 1500s, when an unknown printer took a galley of type and scrambled it to make a type specimen book. It has survived not only five centuries, but also the leap into electronic typesetting, remaining essentially unchanged. It was popularised in the</p>
  <a class="read-more" href="#">Read More</a>
  <div class="slider-controls">
    <span><svg width="10" height="18" viewBox="0 0 10 18"><path d="M8 1 L2 9 L8 17" fill="none" stroke="var(--brand-blue)" stroke-width="2"/></svg></span>
    <span><svg width="10" height="18" viewBox="0 0 10 18"><path d="M2 1 L8 9 L2 17" fill="none" stroke="var(--brand-blue)" stroke-width="2"/></svg></span>
  </div>
</section>

<section class="team">
  <h2 class="heading section-title">OUR TEAM</h2>
  <div class="divider" style="left:475px;top:82px;width:250px">
    <span class="line" style="left:0;width:114px"></span>
    <span class="dot" style="left:119px;background:var(--divider-dark)"></span>
    <span class="line" style="left:135px;width:115px"></span>
  </div>

  <svg class="team-arrow" style="left:130px" width="24" height="44" viewBox="0 0 24 44"><path d="M21 2 L4 22 L21 42" fill="none" stroke="var(--brand-blue)" stroke-width="4"/></svg>

  <div class="member" style="left:176px">
    <div class="portrait light" role="img" aria-label="Portrait photo of team member Elena Brandt">
      <div class="social-band"><i></i><i></i></div>
    </div>
    <div class="member-name">Elena Brandt</div>
    <span class="member-role">Co-Founder</span>
  </div>

  <div class="member" style="left:470px">
    <div class="portrait dark" role="img" aria-label="Portrait photo of team member Tomas Reyes"></div>
    <div class="member-name">Tomas Reyes</div>
    <span class="member-role">Web Developer</span>
  </div>

  <div class="member" style="left:767px">
    <div class="portrait suit" role="img" aria-label="Portrait photo of team member Owen Hartley in a grey suit"></div>
    <div class="member-name">Owen Hartley</div>
    <span class="member-role">Graphic Designer</span>
  </div>

  <svg class="team-arrow" style="left:1043px" width="24" height="44" viewBox="0 0 24 44"><path d="M3 2 L20 22 L3 42" fill="none" stroke="var(--brand-blue)" stroke-width="4"/></svg>
</section>

<div class="footer-edge"></div>
</body>
</html>
```